Coolant Fluid for Radiator BRISK VANE®

Its my first time working with Pixelharbor, and I want to see how it goes:)

We are needing a New exotic label design for our Brisk Vane ® Coolant Fluid for Radiators. Label if possible should be in

Spanish, but its ok if it is in English as we can edit the text later. This label should really stand out!

Front side of label:
Brand Name is BRISK VANE®

It's a Red Type Radiator Fluid/ Liquid. ( This Should Stand out)

It's also Triple action as it works as a Coolant,Anti Rust and Corrosion Inhibitor. It also Protects Aluminuim (Motor Block)

Its Special Red type and chemical composition help mantain the temperature at an optimum level thus preventing Overheating.

Bottle Capacity is 1 liter (Should be on front Label Bottom Right Side)

Back Side of Label:

Properties:
**Emphasizing that the product's Special Red type and chemical composition help mantain the temperature at an optimum

level thus preventing Overheating.
**Emphasize Triple Action (Mentioned above....)
**Will protect Plastic parts, and Connections.
**Mantain Low temperature.
**Prevent and Eliminate Build up of Calcium.

Instruction to use:
1. fill Radiator with BRISK VANE®
2. fill and Mix with Destilled water.

Dosing:
Small Cars 1Liter
Medium Cars 1Liter
Heavy Cars+Heavy Machinery 3Liter

As with almost all fluids for vehicles etc..Label should include safety Hazards.
Such as GHRB label (Please google it) ( Red Blue yellow and White ) Blue box should have a 1 and the others a Zero.

Health and Safety Hazards:
*If swallowed do not Induce vomiting
*seek for medical attention
*Poisonous if consumed
*Keep out of reach of children
(We will add some other things, that we are required to add)
Hazard Symbol Emphazising to read the manufacturer Instructions..

And a Small place where we can place a Barcode/ Recycable Symbol and Dispose of..
Product Registry Code, and Produced and Distributed by Lorem Ipsum etc..

I have attached some Bottle Designs,but dont Restrict yourself on these Bottles, Please keep in mind that the Bottle neck will be placed in the middle of the bottle and not to the sides as with most standard Oil Bottles.
If you have a better Idea/Outline of another bottle dont Hesitate to make a suggestion!

Thanks!
And Sorry my English is not the best :)
hope you have fun Designing this new Label!

Designs should be a little more something like these.. Please check the gallery, I uploaded some samples.. http://snapvault.example/album/zq81rt4k/ These are just for reference.. Regards,

Hi, Please Don't limit yourself to to the shape of the label. If you Think another shape would be better, please do. I will create a special bottle for your label. Thanks!

```html
<!DOCTYPE html>
<html lang="en">
<head>
<meta charset="UTF-8">
<title>Brisk Vane — Radiator Fluid Label</title>
<link rel="stylesheet" href="https://fonts.googleapis.com/css2?family=Bebas+Neue&display=swap">
<style>
  :root {
    --page-bg: #ffffff;
    --label-top: #050102;
    --label-mid: #140406;
    --label-deep: #2a070b;
    --title-steel: #d6d6d8;
    --subtitle-grey: #a9a9ac;
    --accent-yellow: #ffd000;
    --liquid-light: #d8444c;
    --liquid-red: #b81e27;
    --liquid-deep: #5a0a10;
    --text-white: #ffffff;
    --shadow: #000000;
  }
  html, body {
    margin: 0;
    padding: 0;
    width: 831px;
    height: 1200px;
    overflow: hidden;
    background: var(--page-bg);
  }
  .label-canvas { display: block; width: 831px; height: 1200px; }
  .display-type { font-family: "Bebas Neue", "Oswald", sans-serif; }

  .stop-label-top { stop-color: var(--label-top); }
  .stop-label-mid { stop-color: var(--label-mid); }
  .stop-label-deep { stop-color: var(--label-deep); }
  .stop-liquid-light { stop-color: var(--liquid-light); }
  .stop-liquid-red { stop-color: var(--liquid-red); }
  .stop-liquid-deep { stop-color: var(--liquid-deep); }
  .stop-liquid-fade { stop-color: var(--liquid-deep); stop-opacity: 0; }

  .label-shadow { fill: var(--shadow); opacity: 0.35; }
  .brand-name { fill: var(--accent-yellow); }
  .product-type { fill: var(--title-steel); }
  .subtitle { fill: var(--subtitle-grey); }
  .action-count { fill: var(--accent-yellow); }
  .action-line { fill: var(--text-white); }
  .capacity { fill: var(--text-white); }
</style>
</head>
<body>
<svg class="label-canvas" viewBox="0 0 831 1200" xmlns="http://www.w3.org/2000/svg">
  <defs>
    <path id="labelOutline" d="M93,113 Q93,92 114,92 C406,92 649,362 740,522 L740,1085 Q740,1101 722,1101 C406,1085 162,804 93,707 Z"/>
    <clipPath id="labelShape"><use href="#labelOutline"/></clipPath>
    <filter id="softBlur" x="-20%" y="-20%" width="140%" height="140%">
      <feGaussianBlur stdDeviation="6"/>
    </filter>
    <linearGradient id="labelBody" x1="0" y1="0" x2="0" y2="1">
      <stop offset="0" class="stop-label-top"/>
      <stop offset="0.55" class="stop-label-mid"/>
      <stop offset="1" class="stop-label-deep"/>
    </linearGradient>
    <radialGradient id="liquidPool" cx="0.5" cy="0.5" r="0.5">
      <stop offset="0" class="stop-liquid-light"/>
      <stop offset="0.45" class="stop-liquid-red"/>
      <stop offset="0.8" class="stop-liquid-deep"/>
      <stop offset="1" class="stop-liquid-fade"/>
    </radialGradient>
  </defs>

  <use class="label-shadow" href="#labelOutline" transform="translate(6,8)" filter="url(#softBlur)"/>
  <use class="label-body" href="#labelOutline" fill="url(#labelBody)"/>

  <g class="label-art" clip-path="url(#labelShape)">
    <ellipse class="liquid-swirl" role="img" aria-label="Swirling red radiator liquid surface"
             cx="470" cy="820" rx="430" ry="250" fill="url(#liquidPool)"/>
  </g>

  <text class="display-type brand-name" x="312" y="366" font-size="72" text-anchor="middle"
        textLength="270" lengthAdjust="spacingAndGlyphs">BRISK VANE</text>

  <g class="product-title display-type">
    <text class="product-type" x="146" y="566" font-size="184" textLength="491" lengthAdjust="spacingAndGlyphs">RED TYPE</text>
    <text class="subtitle" x="146" y="623" font-size="68" textLength="491" lengthAdjust="spacingAndGlyphs">RADIATOR FLUID/LIQUID</text>
  </g>

  <g class="triple-action display-type">
    <text class="action-count" x="187" y="768" font-size="156" textLength="52" lengthAdjust="spacingAndGlyphs">3</text>
    <text class="action-line" x="247" y="690" font-size="47" textLength="120" lengthAdjust="spacingAndGlyphs">ACTIONS</text>
    <text class="action-line" x="247" y="723" font-size="43" textLength="120" lengthAdjust="spacingAndGlyphs">COOLANT</text>
    <text class="action-line" x="247" y="755" font-size="40" textLength="120" lengthAdjust="spacingAndGlyphs">ANTI RUST</text>
    <text class="action-line" x="247" y="771" font-size="18" textLength="120" lengthAdjust="spacingAndGlyphs">CORROSION INHIBITOR</text>
  </g>

  <text class="capacity display-type" x="618" y="1065" font-size="40" textLength="84" lengthAdjust="spacingAndGlyphs">1 LITER</text>
</svg>
</body>
</html>
```